Flyer for Fundraising Marathon Run for a Charity

Hi. I am running the distance of a marathon race to solicit donations for a charitable cause. I need a well designed flyer to help me solicit support from friends and others. The copy for the flyer is attached. There is a significant amount of written text so it will need to be laid out in a way that is easy to read but also mixes well with some good images and design appeal. I am open to creative ideas. I’ve attached a photo of me from the last time I ran this charity marathon run, the area in Delphi where I will be running and the information for the flyer. These photos don't have to be used if there are animation or drawings that might work with creative appeal. Otherwise, I am open to other stock photos or graphics. Feel free to contact me if you have questions. Thank you !

Industry/Entity Type

Charity

Requirements
Must have
• 8.5 X 11 inches in size

```html
<!DOCTYPE html>
<html lang="en">
<head>
<meta charset="utf-8">
<title>Prayer Run Flyer</title>
<link href="https://fonts.googleapis.com/css2?family=Open+Sans:wght@700;800&family=Arimo:ital,wght@0,400;1,700&display=swap" rel="stylesheet">
<style>
  :root {
    --backdrop: #c6c6c6;
    --paper: #ffffff;
    --ink: #111111;
    --teal: #0aa9ad;
    --teal-deep: #078f93;
    --teal-text: #138d92;
    --purple: #a0199e;
    --link: #9b1a0c;
    --sky: #8cc3ea;
    --hills: #5a6a9a;
    --sea: #4f6fa8;
  }
  * { box-sizing: border-box; margin: 0; padding: 0; }
  html, body { width: 1000px; height: 1200px; overflow: hidden; background: var(--backdrop); }
  .flyer {
    position: absolute; left: 76px; top: 0;
    width: 865px; height: 1224px;
    background: var(--paper);
    transform: scale(0.9804); transform-origin: top left;
    overflow: hidden;
  }
  .hero {
    position: absolute; left: 0; top: 0; width: 865px; height: 305px;
    background: linear-gradient(180deg, var(--sky) 0%, #a7b9d8 28%, var(--hills) 48%, var(--sea) 62%, #6a7892 78%, #7c8a6e 100%);
  }
  .hero-title {
    position: absolute; left: 0; top: 36px; width: 865px;
    text-align: center; color: #fff;
    font-family: "Open Sans", sans-serif; font-weight: 800;
    font-size: 62px; line-height: 62px; letter-spacing: 3px;
    text-shadow: 0 2px 6px rgba(0,0,0,.35);
  }
  .hero-pointer { position: absolute; left: 118px; top: 304px; }
  .intro {
    position: absolute; left: 26px; top: 358px; width: 456px;
    font-family: "Arimo", Arial, sans-serif; font-size: 17px; line-height: 21px;
    color: var(--ink); text-align: justify;
  }
  .intro p { margin-bottom: 21px; }
  .intro p.with-link { margin-bottom: 0; }
  .intro .site { color: var(--link); display: block; margin-bottom: 21px; }
  .tagline {
    position: absolute; left: 515px; top: 330px; width: 336px;
    text-align: center; color: var(--teal-text);
    font-family: "Arimo", Arial, sans-serif; font-style: italic; font-weight: 700;
    font-size: 26px; line-height: 31px;
  }
  .runner-art {
    position: absolute; left: 505px; top: 438px; width: 310px; height: 408px;
    border-radius: 6px;
    background: linear-gradient(160deg, #3a3a3a 0%, #161616 60%, #2b2b2b 100%);
  }
  .steps-panel {
    position: absolute; left: 0; top: 873px; width: 865px; height: 351px;
    background: linear-gradient(180deg, var(--teal) 0%, var(--teal) 55%, var(--teal-deep) 100%);
  }
  .call-banner { position: absolute; left: 0; top: 832px; }
  .call-text {
    position: absolute; left: 21px; top: 844px; width: 680px;
    font-family: "Open Sans", sans-serif; font-weight: 700;
    font-size: 20px; line-height: 25px; color: #fff;
  }
  .panel-pointer { position: absolute; left: 738px; top: 872px; }
  .steps {
    position: absolute; left: 21px; top: 912px; width: 806px;
    list-style: none;
    font-family: "Arimo", Arial, sans-serif; font-size: 17px; line-height: 21px;
    color: #fff; text-align: justify;
  }
  .steps li { margin-bottom: 21px; }
</style>
</head>
<body>
  <main class="flyer">
    <div class="hero" role="img" aria-label="Photo of the mountains and bay around Delphi, Greece"></div>
    <h1 class="hero-title">A SPECIAL JOURNEY<br>FOR YOUR SPECIFIC<br>PRAYERS &amp; FOR AN<br>IMPORTANT ANCIENT</h1>
    <svg class="hero-pointer" width="56" height="30" viewBox="0 0 56 30"><polygon points="0,0 56,0 28,28" fill="#6f7f6c"/></svg>

    <section class="intro">
      <p>This coming April 22 2017 Mark Hollander will make a special running journey of 26 miles through the ancient lands of Apollo and Athena at Delphi on Mt. Parnassus in Greece.</p>
      <p class="with-link">Mark will adorn his running outfit with special cloth strips that will contain written prayers and petitions of people who will sponsor his journey by making a charitable donation to the Hellenic Heritage Union, an organization that preserves the land and the Delphic culture.</p>
      <span class="site">www.hellenic-heritage-union.org</span>
      <p>The concept is simple and very powerful: as Mark runs, your written prayer on a cloth strip will flow and emanate in the wind --- being blessed by the spirits of this ancient and magical land --- asking unto the wind that your prayer be answered.  This type of prayer practice dates back to ancient times.  The Tibetan culture commonly uses prayer flags with special mantras and symbols.</p>
    </section>

    <p class="tagline">Your Prayer Can Make A Difference For You &amp; For A Good Cause !</p>
    <div class="runner-art" role="img" aria-label="Silhouette illustration of a runner trailing colourful prayer ribbons"></div>

    <div class="steps-panel"></div>
    <svg class="call-banner" width="707" height="68" viewBox="0 0 707 68"><polygon points="0,0 707,0 686,68 0,68" fill="var(--purple)"/></svg>
    <p class="call-text">Will you make a prayer for yourself or a loved and support a good cause? Here is how to get your prayer started:</p>
    <svg class="panel-pointer" width="60" height="32" viewBox="0 0 60 32"><polygon points="0,0 60,0 30,30" fill="#fff"/></svg>

    <ol class="steps">
      <li>1)  Decide what you want your prayer, petition or intention to be.</li>
      <li>2)  Define your prayer, petition or intention by writing it down.</li>
      <li>3)  Refine it is concise, clear &amp; specific. (18 words or less is ideal for each strip cloth).</li>
      <li>4)  Contact Mark at mhollander@hollanderreyes.com and tell him how many prayer cloth strips you wish to obtain. Mark will then send you the cloth for you to write your prayer and send back to him or he will write out the prayer for you. Mark can also answer any questions you may have.</li>
      <li>5)  A minimum donation of $25 for each prayer cloth is requested.  Checks can be made to the “Mark Hollander/Hellenic Heritage Union” and mail to Mark T. Hollander, Hollander Reyes PLC, 4127 Elm Avenue, Ste. 204 Lakeside, Virginia 23999 or though online payment instructions sent by email from Mark as requested.</li>
    </ol>
  </main>
</body>
</html>
```